依頼詳細
◇サイトマップ
①Home ※メニューページ・代表あいさつ・アクセス・ブログレコメンド SNSはリンク・無料相談を打ち出す
② 選ばれる理由※コンセプト
③ 事業案内
④ 事業所概要
⑤ 料金 ※相談無料・その他料金
⑥ よくある質問 ※カテゴリ分け
⑦ お問い合わせ ※お問い合わせフォーム
⑧代表紹介
⑨ブログ(一覧・詳細) ※サイト内ブログ・カテゴリ作成
⑩ニュース(一覧・詳細) ※サイト内ブログ
⑪ 不動産登記
⑫相続
⑬遺言
⑭成年後見
⑮ 家族信託
⑯商業登記
⑰お客様の声 ※アンケート
⑱ビジネスパートナー ※項目名は変える

◇優先事項
1.ユーザビリティー
2.凝ったデザイン
3.編集更新

◇期待する効果
1.売上の向上
2.新規顧客の獲得
3.問い合わせ数の向上

◇ターゲット
【性別】男女比(男6 : 4女)
【年代】30代~50代
【属性】会社員 自営業(経営者) その他として士業の方

◇sns
Instagram  個人用
Facebook  会社用
Twitter   会社用
LINE 今後やるかも

◇テイスト
ナチュラル 優しい 清潔感
サイトURL
http://k-tomoe.net/index.html
ページ数
1ページ
希望イメージ
シンプル 複雑
単色 カラフル
暗い 明るい
日常 高級
遊び心 厳粛
未来的 伝統的
女性的 男性的
希望する色
青系、ベースは白系が良いです。 水色 グレー系やミドリ系があっても良いかも。
納品ファイル
• イラストレーター形式 (.ai)
• フォトショップ形式 (.psd)
• PNG形式 (.png)
補足説明
素材①
店内写真などをベルトラックスを使って、アップしています。
下記URLよりダウンロードしてください。
■ダウンロードURL:http://beltrax.jp/download/4c81e02b9d3f6a17e5b0c2d8a94f61e3b07d5c29
ダウンロードパスワード pass

素材②
ピクモル:https://jp.picmolle.com/
当社で定期契約をしています。クレジット購入のみのもの以外をご利用下さい。
また定期契約のものは弊社の負担となり、ランサー様に負担はありません。
カンプ画像を入れてください。

素材③
現行サイトより引用してください。
URL:http://k-tomoe.net/index.html
画像やテキストに関しては一旦引き抜いて頂いて構いません。
延長を行わせて頂きます。
宜しくお願いたします。
提案を延長させて頂きます。
理由として、全体のテイストが、いかにも、司法書士事務所のという感じで、
なんとなく近寄りがたい印象があります・・

https://meigawari.sitebako.com/
上記のようなイメージでお願いできればと思います。

https://www.kogure-hoki.com/index.html
上記のサイトになるとやりすぎている印象はありますが、テイストとして取り入れて頂きたいです。
現状の経営理念に近い考え方が「今を楽しみ、未来につなぐ」になるため、デザイン作成時に参考にして頂ければと思います!

デザインがイメージ通りに上がってきた為、選定をさせた頂きました。
修正の対応も丁寧にまとめていただいたり、適切な質問を頂き非常に進行が行いやすかったです。
ありがとうございました。

途中でテイストが変わってしまいましたが、お付き合い頂いたランサー様が多く非常に助かりました。感謝致します。
選定出来なかった皆様にこころ苦しい気持ちでいっぱいです。
ありがとうございました。

```html
<!DOCTYPE html>
<html lang="ja">
<head>
<meta charset="utf-8">
<title>ひなた法務司法書士事務所</title>
<link href="https://fonts.googleapis.com/css2?family=Noto+Sans+JP:wght@400;500;700&family=Noto+Serif+JP:wght@500;700&display=swap" rel="stylesheet">
<style>
:root{
  --blue:#2f6db5;
  --blue-dark:#1f4f8c;
  --blue-soft:#e8f1fa;
  --sky:#9cc4e6;
  --grey:#f4f6f8;
  --line:#d9e1ea;
  --text:#333a42;
  --muted:#7a838d;
  --white:#ffffff;
  --yellow:#f3d64b;
}
*{box-sizing:border-box;margin:0;padding:0}
html,body{width:1200px;height:3636px;overflow:hidden}
body{font-family:"Noto Sans JP",sans-serif;color:var(--text);background:var(--white);font-size:14px;line-height:1.7}
.wrap{width:1000px;margin:0 auto;position:relative}

/* header */
.site-header{height:66px;display:flex;align-items:center;justify-content:space-between;padding:0 24px;background:var(--white);white-space:nowrap}
.brand{display:flex;align-items:center;gap:10px}
.brand-mark{width:32px;height:32px;background:var(--blue);border-radius:4px;flex:none}
.brand-name{font-size:16px;font-weight:700;color:var(--blue-dark);line-height:1.25;white-space:nowrap}
.brand-name small{display:block;font-size:10px;font-weight:400;color:var(--muted)}
.global-nav{display:flex}
.global-nav a{font-size:12px;color:var(--text);text-decoration:none;padding:0 9px;border-left:1px solid var(--line);line-height:1.3;white-space:nowrap}
.global-nav a:last-child{border-right:1px solid var(--line)}
.global-nav a:first-child{color:var(--blue)}
.header-contact{display:flex;align-items:center;gap:10px}
.free-badge{background:var(--blue);color:var(--white);font-size:10px;padding:4px 6px;line-height:1.2;text-align:center}
.tel{font-size:20px;font-weight:700;color:var(--blue-dark);line-height:1.1;white-space:nowrap}
.tel small{display:block;font-size:10px;font-weight:400;color:var(--muted)}
.btn-mail{background:var(--blue);color:var(--white);font-size:11px;padding:6px 12px;border-radius:3px;white-space:nowrap}

/* hero */
.hero{position:relative;height:456px}
.hero-photo{position:absolute;inset:0;background:linear-gradient(100deg,#d7dde4 0%,#eef1f4 40%,#f3e6df 70%,#c9d8e6 100%)}
.hero-copy{position:absolute;left:50%;top:50%;transform:translate(-50%,-50%);width:330px;height:330px;border-radius:50%;background:rgba(255,255,255,.92);display:flex;flex-direction:column;align-items:center;justify-content:center;text-align:center}
.hero-copy .mark{width:44px;height:44px;background:var(--blue);border-radius:4px;margin-bottom:14px}
.hero-copy h1{font-family:"Noto Serif JP",serif;font-size:30px;color:var(--blue-dark);line-height:1.35;font-weight:700}
.hero-copy p{font-size:12px;margin-top:12px;color:var(--text)}

/* consult */
.consult{padding:40px 0 50px;background:var(--white)}
.consult-head{position:relative;height:150px}
.consult-head h2{font-size:24px;color:var(--blue-dark);font-weight:700;padding-left:110px;padding-top:30px}
.consult-head p{font-size:13px;padding-left:110px;margin-top:6px}
.consult-person{position:absolute;right:90px;top:0;width:110px;height:150px;background:linear-gradient(#cdd8e3,#9fb0c1);border-radius:4px}
.service-grid{display:grid;grid-template-columns:repeat(3,1fr);gap:26px;margin-top:12px}
.service-card{background:var(--white);border:1px solid var(--line);box-shadow:0 2px 6px rgba(40,80,130,.08);padding:22px 24px 24px;text-align:center;height:188px}
.service-card svg{width:44px;height:44px}
.service-card h3{font-size:17px;color:var(--blue-dark);margin:6px 0 10px}
.service-card ul{list-style:none;text-align:left;font-size:12px;line-height:1.9}
.service-card li::before{content:"";display:inline-block;width:8px;height:8px;background:var(--blue);margin-right:8px;vertical-align:1px}

/* greeting */
.greeting{position:relative;height:440px;background:var(--grey)}
.greeting-photo{position:absolute;right:0;top:0;width:560px;height:100%;background:linear-gradient(90deg,#eef1f4 0%,#d5dbe2 35%,#bcc8d4 100%)}
.greeting-body{position:absolute;left:100px;top:50px;width:520px}
.greeting-body h2{font-size:22px;color:var(--blue-dark)}
.greeting-body h2 span{font-size:11px;color:var(--muted);margin-left:10px;font-weight:400}
.greeting-body .lead{font-family:"Noto Serif JP",serif;font-size:19px;color:var(--blue);margin:18px 0 14px;font-weight:700}
.greeting-body p{font-size:12px;line-height:2}
.signature{margin-top:14px;text-align:right;font-size:13px}
.signature strong{font-family:"Noto Serif JP",serif;font-size:20px;margin-left:10px}
.btn-blue{display:inline-block;background:var(--blue);color:var(--white);font-size:12px;padding:8px 28px;border-radius:3px;margin-top:18px}

/* blog */
.blog{position:relative;height:410px;background:linear-gradient(var(--blue),#5f92c8);overflow:hidden}
.blog-bg{position:absolute;inset:0;background:linear-gradient(180deg,rgba(47,109,181,.85),rgba(80,140,200,.85))}
.section-title{text-align:center;font-size:22px;font-weight:700}
.section-title span{display:block;font-size:11px;font-weight:400;opacity:.8}
.blog .section-title{color:var(--white);padding-top:38px}
.blog-list{display:grid;grid-template-columns:repeat(3,1fr);gap:24px;width:880px;margin:26px auto 0}
.blog-card{background:var(--white);padding:10px}
.blog-thumb{height:130px;background:linear-gradient(#e5e9ee,#c7d1dc)}
.blog-card time{display:block;font-size:11px;color:var(--muted);margin-top:8px}
.blog-card h3{font-size:13px;font-weight:500}
.blog-card .more{display:block;width:110px;margin:10px auto 2px;background:var(--blue);color:var(--white);font-size:11px;text-align:center;padding:4px 0;border-radius:2px}

/* news */
.news{height:530px;padding-top:46px}
.news .section-title{color:var(--text)}
.news-list{width:820px;margin:26px auto 0;list-style:none}
.news-list li{display:flex;gap:26px;border-bottom:1px solid var(--line);padding:10px 6px;font-size:12px}
.news-list time{font-weight:700;width:80px}
.news-list .cat{background:var(--blue);color:var(--white);font-size:10px;padding:1px 8px;height:18px;line-height:16px}
.news .btn-blue{display:block;width:170px;margin:24px auto 0;text-align:center}

/* contact band */
.cta{position:relative;height:250px;background:var(--blue);overflow:hidden;color:var(--white)}
.cta-photo{position:absolute;right:0;top:0;width:560px;height:100%;background:linear-gradient(90deg,#5d8ec4,#c8d3de 45%,#dfe5ea)}
.cta-body{position:absolute;left:100px;top:34px}
.cta-body h2{font-size:26px;font-weight:700}
.cta-tel{display:flex;align-items:center;gap:14px;margin-top:14px}
.cta-tel .num{font-size:30px;font-weight:700;line-height:1;white-space:nowrap}
.cta-tel .num small{display:block;font-size:10px;font-weight:400;margin-top:4px}
.cta-tel .btn-mail{background:var(--white);color:var(--blue);font-size:12px;padding:8px 14px}
.cta-days{margin-top:18px;font-size:18px;font-weight:700;color:var(--yellow)}

/* footer */
.site-footer{height:270px;padding-top:44px;background:var(--white)}
.footer-inner{display:flex;justify-content:space-between;width:1000px;margin:0 auto}
.footer-info .brand{margin-bottom:14px}
.footer-info p{font-size:12px;line-height:1.85}
.sns{display:flex;gap:12px;margin-top:14px}
.sns span{width:28px;height:28px;border-radius:50%;background:var(--blue)}
.footer-links{display:flex;gap:60px}
.footer-links ul{list-style:none;font-size:12px;line-height:2}
.footer-links li::before{content:"› ";color:var(--blue)}

.map{height:494px;background:linear-gradient(135deg,#e6e9e4,#d8dee6 60%,#c9d9ea)}
.copyright{height:36px;background:var(--blue-dark);color:var(--white);font-size:11px;text-align:center;line-height:36px}
</style>
</head>
<body>

<header class="site-header">
  <div class="brand">
    <span class="brand-mark"></span>
    <div class="brand-name"><small>司法書士・行政書士</small>ひなた法務司法書士事務所</div>
  </div>
  <nav class="global-nav">
    <a href="#">ホーム</a>
    <a href="#">選ばれる理由</a>
    <a href="#">事業案内</a>
    <a href="#">事務所概要</a>
    <a href="#">料金</a>
    <a href="#">よくある質問</a>
    <a href="#">お客様の声</a>
    <a href="#">ブログ</a>
  </nav>
  <div class="header-contact">
    <div class="free-badge">相談<br>無料</div>
    <div class="tel">06-6123-4567<small>受付時間 平日9:00〜18:00</small></div>
    <span class="btn-mail">メールでお問い合わせ</span>
  </div>
</header>

<section class="hero">
  <div class="hero-photo" role="img" aria-label="電話応対する司法書士と家族の写真"></div>
  <div class="hero-copy">
    <span class="mark"></span>
    <h1>「なんでも話せる」<br>存在でありたい</h1>
    <p>スモールワールドを目指し、<br>トラブルを未然に防ぐ手伝いをいたします</p>
  </div>
</section>

<section class="consult">
  <div class="wrap">
    <div class="consult-head">
      <h2>こんなときは司法書士にご相談ください！</h2>
      <p>トラブルを未然に防ぐプロが お悩みを一緒に解決いたします。</p>
      <div class="consult-person" role="img" aria-label="本を持つ司法書士の写真"></div>
    </div>
    <div class="service-grid">
      <article class="service-card">
        <svg viewBox="0 0 44 44"><path d="M6 22 22 8l16 14v16H28V28h-12v10H6z" fill="var(--blue)"/></svg>
        <h3>不動産登記</h3>
        <ul><li>土地を購入したい</li><li>住宅ローンを完済した</li></ul>
      </article>
      <article class="service-card">
        <svg viewBox="0 0 44 44"><circle cx="15" cy="14" r="6" fill="var(--blue)"/><circle cx="29" cy="14" r="6" fill="var(--blue)"/><path d="M4 36c0-9 5-13 11-13s11 4 11 13zM18 36c0-9 5-13 11-13s11 4 11 13z" fill="var(--blue)"/></svg>
        <h3>相続</h3>
        <ul><li>亡くなった方の財産を整理したい</li><li>相続人の確認がしたい</li></ul>
      </article>
      <article class="service-card">
        <svg viewBox="0 0 44 44"><rect x="10" y="6" width="24" height="32" rx="2" fill="var(--blue)"/><path d="M15 15h14M15 21h14M15 27h9" stroke="#fff" stroke-width="2"/></svg>
        <h3>遺言</h3>
        <ul><li>遺言書を作成したい</li><li>遺言書の内容を確認したい</li></ul>
      </article>
      <article class="service-card">
        <svg viewBox="0 0 44 44"><circle cx="22" cy="13" r="7" fill="var(--blue)"/><path d="M8 38c0-10 6-15 14-15s14 5 14 15z" fill="var(--blue)"/></svg>
        <h3>成年後見</h3>
        <ul><li>親の財産管理が心配</li><li>将来に備えて準備したい</li></ul>
      </article>
      <article class="service-card">
        <svg viewBox="0 0 44 44"><path d="M22 38 6 22a8 8 0 0 1 16-10 8 8 0 0 1 16 10z" fill="var(--blue)"/></svg>
        <h3>家族信託</h3>
        <ul><li>家族に財産の管理を任せたい</li><li>認知症に備えたい</li></ul>
      </article>
      <article class="service-card">
        <svg viewBox="0 0 44 44"><rect x="8" y="10" width="28" height="28" fill="var(--blue)"/><path d="M14 16h4v4h-4zM26 16h4v4h-4zM14 24h4v4h-4zM26 24h4v4h-4zM20 30h4v8h-4z" fill="#fff"/></svg>
        <h3>商業登記</h3>
        <ul><li>会社を設立したい</li><li>役員を変更したい</li></ul>
      </article>
    </div>
  </div>
</section>

<section class="greeting">
  <div class="greeting-photo" role="img" aria-label="微笑む代表司法書士の写真"></div>
  <div class="greeting-body">
    <h2>代表あいさつ<span>GREETING</span></h2>
    <p class="lead">「なんでも話せる」目線のベストパートナーでありたい</p>
    <p>「今を楽しみ、未来につなぐ」を理念に、ご相談者様の声に耳を傾けています。司法書士は登記の専門家ですが、それ以上に身近な相談相手でありたいと考えています。小さなお悩みでも、どうぞお気軽にお声がけください。</p>
    <p>地域の皆様の暮らしと事業を守るため、わかりやすい説明と丁寧な対応を心がけてまいります。</p>
    <div class="signature">代表司法書士<strong>早瀬 和成</strong></div>
    <span class="btn-blue">代表プロフィール ›</span>
  </div>
</section>

<section class="blog">
  <div class="blog-bg" role="img" aria-label="街並みと橋の写真"></div>
  <div style="position:relative">
    <h2 class="section-title">厳選ブログ<span>BLOG</span></h2>
    <div class="blog-list">
      <article class="blog-card">
        <div class="blog-thumb" role="img" aria-label="事務所入口の写真"></div>
        <time>2017年12月1日</time>
        <h3>ブログタイトルがここに入ります</h3>
        <span class="more">詳しく見る ›</span>
      </article>
      <article class="blog-card">
        <div class="blog-thumb" role="img" aria-label="打ち合わせ室の写真"></div>
        <time>2017年12月1日</time>
        <h3>ブログタイトルがここに入ります</h3>
        <span class="more">詳しく見る ›</span>
      </article>
      <article class="blog-card">
        <div class="blog-thumb" role="img" aria-label="相談の様子の写真"></div>
        <time>2017年12月1日</time>
        <h3>ブログタイトルがここに入ります</h3>
        <span class="more">詳しく見る ›</span>
      </article>
    </div>
  </div>
</section>

<section class="news">
  <h2 class="section-title">お知らせ<span>NEWS</span></h2>
  <ul class="news-list">
    <li><time>2017.12.01</time><span class="cat">お知らせ</span>年末年始休業のお知らせです。詳細はこちらをご確認ください。</li>
    <li><time>2017.11.20</time><span class="cat">お知らせ</span>無料相談会を開催いたします。ご予約をお待ちしております。</li>
    <li><time>2017.11.08</time><span class="cat">お知らせ</span>ホームページをリニューアルいたしました。</li>
    <li><time>2017.10.25</time><span class="cat">お知らせ</span>相続登記に関するセミナーのご案内です。</li>
    <li><time>2017.10.11</time><span class="cat">お知らせ</span>夏季休業のお知らせです。詳細はこちらをご確認ください。</li>
    <li><time>2017.09.30</time><span class="cat">お知らせ</span>家族信託の相談窓口を新設いたしました。</li>
    <li><time>2017.09.12</time><span class="cat">お知らせ</span>事務所の営業時間を変更いたしました。</li>
  </ul>
  <span class="btn-blue">お知らせ一覧 ›</span>
</section>

<section class="cta">
  <div class="cta-photo" role="img" aria-label="相談者と話す司法書士の写真"></div>
  <div class="cta-body">
    <h2>ご相談は無料であります！</h2>
    <div class="cta-tel">
      <div class="num">06-6123-4567<small>受付時間 平日9:00〜18:00</small></div>
      <span class="btn-mail">メールでお問い合わせ</span>
    </div>
    <p class="cta-days">土・日・祝 相談可能（要予約）</p>
  </div>
</section>

<footer class="site-footer">
  <div class="footer-inner">
    <div class="footer-info">
      <div class="brand">
        <span class="brand-mark"></span>
        <div class="brand-name"><small>司法書士・行政書士</small>ひなた法務司法書士事務所</div>
      </div>
      <p>〒540-0000<br>大阪府大阪市北浜区1-2-3 ひなたビル5階<br>TEL 06-6123-4567　FAX 06-6123-4568<br>受付時間 平日9:00〜18:00（土日祝は要予約）</p>
      <div class="sns"><span></span><span></span><span></span><span></span></div>
    </div>
    <div class="footer-links">
      <ul><li>HOME</li><li>選ばれる理由</li><li>事業案内</li><li>事務所概要</li><li>料金</li><li>よくある質問</li><li>お問い合わせ</li></ul>
      <ul><li>代表紹介</li><li>ブログ</li><li>ニュース</li><li>お客様の声</li><li>ビジネスパートナー</li><li>サイトマップ</li></ul>
    </div>
  </div>
</footer>

<div class="map" role="img" aria-label="事務所周辺の地図"></div>
<div class="copyright">© ひなた法務司法書士事務所 All Rights Reserved.</div>

</body>
</html>
```